Business Card Design

Velvet Pixel Promotions

An online marketing consulting & strategy business for the cosmetic niche

We specialise in Increasing Leads, Conversions & Content Marketing

I am looking for a very clean, BOLD business card that is simple & effective

Target Market(s)

cosmetic surgeons & cosmetic clinics

Industry/Entity Type

Marketing

Contact Information for Business Card

Darren Okoye
Online Marketing Strategist

Darren@VelvetPixelPromotions.example
0491 268 517

LinkedIn: in/darrenokoye

```html
<!DOCTYPE html>
<html lang="en">
<head>
<meta charset="utf-8">
<title>Velvet Pixel Promotions — Business Card</title>
<link rel="stylesheet" href="https://fonts.googleapis.com/css2?family=Roboto:ital,wght@0,400;0,500;1,400&display=swap">
<style>
  :root {
    --page-bg: #e9e9e9;
    --card-bg: #ffffff;
    --ink-grey: #5f6062;
    --ink-soft: #4a4a4a;
    --brand-green: #5cb82e;
    --brand-teal: #1ea8d8;
    --band-lime: #b5d334;
    --band-blue: #1b9ed6;
    --band-green: #3fb46b;
    --card-shadow: 0 6px 18px rgba(0,0,0,0.18);
  }
  * { margin: 0; padding: 0; box-sizing: border-box; }
  html, body {
    width: 1200px; height: 1000px; overflow: hidden;
    background: var(--page-bg);
    font-family: "Roboto", Arial, sans-serif;
  }
  .stage { position: relative; width: 1200px; height: 1000px; }

  .card {
    position: absolute;
    width: 645px; height: 372px;
    background: var(--card-bg);
    box-shadow: var(--card-shadow);
    overflow: hidden;
  }
  .card--front { left: 120px; top: 100px; }
  .card--back  { left: 435px; top: 528px; }

  /* Brand lockup */
  .brand { display: flex; align-items: center; color: var(--ink-grey); }
  .brand__dot { flex: none; border-radius: 50%; background: var(--brand-teal); }
  .brand__name {
    font-weight: 500; text-transform: uppercase;
    color: var(--ink-grey); line-height: 0.98;
  }

  .card--front .brand {
    position: absolute; left: 130px; top: 118px; gap: 26px;
  }
  .card--front .brand__dot { width: 92px; height: 92px; }
  .card--front .brand__name { font-size: 45px; letter-spacing: 3px; }

  .card--back .brand {
    position: absolute; left: 44px; top: 100px; gap: 12px;
  }
  .card--back .brand__dot { width: 44px; height: 44px; }
  .card--back .brand__name { font-size: 21px; letter-spacing: 1.4px; }

  /* Contact block */
  .contact { position: absolute; left: 337px; top: 98px; }
  .contact__name { font-size: 23px; font-weight: 400; color: var(--brand-green); }
  .contact__role { font-size: 14.5px; font-style: italic; color: var(--ink-soft); margin-top: 4px; }
  .contact__list { list-style: none; margin-top: 26px; }
  .contact__item {
    display: flex; align-items: center; gap: 9px;
    font-size: 14.5px; color: var(--ink-soft); height: 21px;
  }
  .contact__icon { width: 18px; height: 14px; flex: none; }
  .contact__square { width: 15px; height: 15px; background: var(--brand-green); border-radius: 2px; margin: 0 1.5px; flex: none; }

  .pattern-band {
    position: absolute; left: 0; bottom: 0; width: 100%; height: 60px;
    background: linear-gradient(90deg, var(--band-blue), var(--band-green) 45%, var(--band-lime) 70%, var(--band-blue));
  }
</style>
</head>
<body>
<main class="stage">

  <section class="card card--front" aria-label="Card front">
    <div class="brand">
      <span class="brand__dot"></span>
      <span class="brand__name">Velvet<br>Pixel<br>Promotions</span>
    </div>
  </section>

  <section class="card card--back" aria-label="Card back">
    <div class="brand">
      <span class="brand__dot"></span>
      <span class="brand__name">Velvet<br>Pixel<br>Promotions</span>
    </div>

    <div class="contact">
      <h1 class="contact__name">Darren Okoye</h1>
      <p class="contact__role">Online Marketing Strategist</p>
      <ul class="contact__list">
        <li class="contact__item">
          <svg class="contact__icon" viewBox="0 0 18 14" aria-hidden="true">
            <path d="M1 5 Q9 -1 17 5 L15 7 L12 5.5 L12 4 Q9 3 6 4 L6 5.5 L3 7 Z" fill="#5cb82e"/>
            <rect x="4" y="7" width="10" height="6" rx="1.5" fill="#5cb82e"/>
            <circle cx="9" cy="10" r="1.6" fill="#fff"/>
          </svg>
          0491 268 517
        </li>
        <li class="contact__item">
          <svg class="contact__icon" viewBox="0 0 18 14" aria-hidden="true">
            <rect x="1" y="1.5" width="16" height="11" rx="1" fill="#5cb82e"/>
            <path d="M1.5 2.5 L9 8.5 L16.5 2.5" fill="none" stroke="#fff" stroke-width="1.3"/>
          </svg>
          Darren@VelvetPixelPromotions.example
        </li>
        <li class="contact__item">
          <span class="contact__square"></span>
          /darrenokoye
        </li>
      </ul>
    </div>

    <div class="pattern-band" role="img" aria-label="Decorative band of blue, green and lime geometric diamonds"></div>
  </section>

</main>
</body>
</html>
```